Poetry Book Cover Design Project

Looking for a minimalistic book cover design for a collection of poems. The book title is "Before The Morning Turns To Glass". There are three parts to the book. First covers poetry in the theme of Rage. Second love and desire. The third is strange poems. Essentially the sections are "Rage", "Desire" and the "Strange". The reason for the title "Before The Morning Turns To Glass" is as if someone is writing these till life changes towards the intended outcome as felt in each poem. I want to have the author's name "Nirosha Kulathunge" at the bottom. Ilustration attached.
- Minimalistic

```html
<!DOCTYPE html>
<html lang="en">
<head>
<meta charset="utf-8">
<title>Before The Morning Turns To Glass — Cover</title>
<link rel="stylesheet" href="https://fonts.googleapis.com/css2?family=Cormorant+Garamond:ital,wght@1,500&family=Tenor+Sans&display=swap">
<style>
  :root {
    --backdrop: #4a433d;
    --paper: #efece6;
    --paper-shade: #e2ded6;
    --title-ink: #55524f;
    --author-red: #8c1d12;
    --sun-gold: #d9b160;
    --sun-gold-pale: #ebdcb4;
    --leaf-red: #c0462a;
  }
  * { margin: 0; padding: 0; box-sizing: border-box; }
  html, body {
    width: 1200px;
    height: 800px;
    overflow: hidden;
    background: var(--backdrop);
  }
  .stage {
    width: 1200px;
    height: 800px;
    display: flex;
    align-items: center;
    justify-content: center;
  }
  .cover {
    position: relative;
    width: 505px;
    height: 740px;
    overflow: hidden;
    background: radial-gradient(ellipse at 60% 40%, var(--paper) 0%, var(--paper) 55%, var(--paper-shade) 100%);
  }
  .sunburst-art {
    position: absolute;
    left: 0;
    top: 160px;
    width: 200px;
    height: 360px;
    background: linear-gradient(90deg, var(--sun-gold) 0%, var(--sun-gold-pale) 100%);
  }
  .leaf-art {
    position: absolute;
    left: 180px;
    top: 160px;
    width: 70px;
    height: 70px;
    background: var(--leaf-red);
  }
  .title {
    position: absolute;
    right: 52px;
    top: 80px;
    font-family: "Cormorant Garamond", Georgia, serif;
    font-style: italic;
    font-weight: 500;
    font-size: 68px;
    line-height: 86px;
    color: var(--title-ink);
    text-align: right;
    letter-spacing: 1px;
  }
  .title span { display: block; }
  .title .line-2, .title .line-4 { padding-right: 44px; }
  .title .line-6 { padding-right: 4px; }
  .author {
    position: absolute;
    left: 0;
    right: 0;
    bottom: 52px;
    padding-left: 150px;
    text-align: center;
    font-family: "Tenor Sans", "Helvetica Neue", sans-serif;
    font-size: 22px;
    letter-spacing: 0.5px;
    color: var(--author-red);
  }
</style>
</head>
<body>
  <main class="stage">
    <section class="cover">
      <div class="sunburst-art" role="img" aria-label="Illustration: golden sunburst around a dark blue eclipse disc, cut by the left edge"></div>
      <div class="leaf-art" role="img" aria-label="Illustration: single red autumn maple leaf"></div>
      <h1 class="title">
        <span class="line-1">Before</span>
        <span class="line-2">The</span>
        <span class="line-3">Morning</span>
        <span class="line-4">Turns</span>
        <span class="line-5">To</span>
        <span class="line-6">Glass</span>
      </h1>
      <p class="author">Nirosha Kulathunge</p>
    </section>
  </main>
</body>
</html>
```